Brightwave Scanning Partners, LLC
"we bring a quality ultrasound to you"
Professional
Doriane Fallowby
Director of Marketing
Fernvale, NJ
info@brightwavescanningpartners.net
www.brightwavescanningpartners.net

```html
<!DOCTYPE html>
<html lang="en">
<head>
<meta charset="utf-8">
<title>Brightwave Scanning Partners – Business Card</title>
<link href="https://fonts.googleapis.com/css2?family=Arimo:wght@400;700&display=swap" rel="stylesheet">
<style>
  :root {
    --backdrop: #5b3020;
    --card-white: #ffffff;
    --brand-purple: #9c2a8c;
    --brand-blue: #1aa3e0;
    --name-purple: #7d2a7e;
    --text-white: #ffffff;
  }
  html, body {
    margin: 0;
    padding: 0;
    width: 1200px;
    height: 965px;
    overflow: hidden;
    background: var(--backdrop);
    font-family: "Arimo", Arial, sans-serif;
  }
  .business-card {
    position: absolute;
    left: 100px;
    top: 198px;
    width: 1000px;
    height: 568px;
    border-radius: 26px;
    overflow: hidden;
    background: var(--card-white);
    box-shadow: 0 10px 28px rgba(0,0,0,0.35);
  }
  .card-shapes {
    position: absolute;
    inset: 0;
  }
  .holder {
    position: absolute;
    left: 32px;
    top: 26px;
    color: var(--text-white);
  }
  .holder-name {
    margin: 0;
    font-size: 32px;
    font-weight: 700;
    line-height: 1.15;
  }
  .holder-title {
    margin: 2px 0 0;
    font-size: 24px;
    font-weight: 400;
  }
  .contact {
    position: absolute;
    left: 32px;
    top: 400px;
    margin: 0;
    padding: 0;
    list-style: none;
    color: var(--text-white);
    font-size: 24px;
    line-height: 34px;
  }
  .contact .label {
    font-weight: 700;
  }
  .company-name {
    position: absolute;
    left: 660px;
    top: 215px;
    width: 320px;
    display: flex;
    align-items: center;
    gap: 16px;
  }
  .company-dot {
    flex: none;
    width: 26px;
    height: 26px;
    border-radius: 50%;
    background: var(--brand-blue);
  }
  .company-text {
    margin: 0;
    font-size: 34px;
    font-weight: 700;
    line-height: 1.1;
    color: var(--name-purple);
  }
</style>
</head>
<body>
  <div class="business-card">
    <svg class="card-shapes" viewBox="0 0 1000 568" width="1000" height="568" aria-hidden="true">
      <path d="M0 0 H628 C 526 180, 526 400, 670 568 H0 Z" fill="var(--brand-blue)"/>
      <path d="M0 0 H602 C 500 180, 500 400, 642 568 H0 Z" fill="var(--brand-purple)"/>
    </svg>

    <div class="holder">
      <h1 class="holder-name">Doriane Fallowby</h1>
      <p class="holder-title">Director of Marketing</p>
    </div>

    <ul class="contact">
      <li>Fernvale, NJ</li>
      <li><span class="label">Phone</span> : 555-014-2273</li>
      <li><span class="label">Email</span> : info@brightwavescanningpartners.net</li>
      <li><span class="label">Web</span> : www.brightwavescanningpartners.net</li>
    </ul>

    <div class="company-name">
      <span class="company-dot"></span>
      <p class="company-text">Brightwave Scanning Partners, LLC</p>
    </div>
  </div>
</body>
</html>
```